Birthday Calendar: Dec 1 - Nov 30

This calendar should have three parts. First the center should contain an annual calendar beginning December 1, 2019 and going through November 30, 2020. I'm picturing the months and date numbers - no need for individual boxes for each day. Second, above the calendar should be blank space (intended for people to write words of advise and love). Third, beneath the calendar space will be several statements about the year (i.e. "If you have client meetings four times a month, you'll meet with 36 clients." "If you kiss your kids only once each day, that's 1,460 kisses.") I don't have an exact overall size of the calendar in mind, but definitely know it will need to be bigger than 8.5"x11"

Target Market(s)

Wife - Her birthday is November 30, so this is a calendar to mark the time from one birthday to the next.

Font styles to use
Serif

Colors

Designer to choose colors to be used in the design.

Requirements
Must have
• The three different sections listed in the description. There will be 12 people handwriting simple phrases of advise (for how to have the best year) at the top, so there should be enough room for that. At the top it should say "These are the Days"
• I will provide the complete set of statements that will appear at the bottom of the calendar. There will be 10 (or less) statements total, sort of like the ones provided in the description. Let me know when you want those statements.

```html
<!DOCTYPE html>
<html lang="en">
<head>
<meta charset="utf-8">
<title>These are the days – Birthday Year Calendar</title>
<link href="https://fonts.googleapis.com/css2?family=Kaushan+Script&family=Yellowtail&family=Playfair+Display:wght@900&family=Roboto:ital,wght@0,300;0,400;0,700;1,400;1,700;1,900&family=Lora:ital@1&display=swap" rel="stylesheet">
<style>
  :root{
    --backdrop:#2d5ea9;
    --paper:#dcefef;
    --note:#f3f4f5;
    --ink:#1b1b1b;
    --band:#3a346e;
    --white:#ffffff;
    --sky:#2fa8dc;
    --magenta:#e5198b;
    --lemon:#f2e731;
    --orange:#f7941d;
    --lime:#8cc63f;
    --red:#e8262b;
  }
  *{box-sizing:border-box;margin:0;padding:0}
  html,body{width:1180px;height:1200px;overflow:hidden;background:var(--backdrop)}
  .poster{position:absolute;left:129px;top:20px;width:921px;height:1160px;background:var(--paper);overflow:hidden}

  .headline{position:absolute;top:26px;left:58px;width:806px;display:flex;align-items:center;justify-content:center;gap:16px}
  .headline .rule{flex:1;height:1.5px;background:var(--ink)}
  .headline h1{font-family:"Kaushan Script","Yellowtail",cursive;font-weight:400;font-size:44px;color:var(--ink);line-height:1.2;white-space:nowrap}

  .wishes{position:absolute;left:58px;top:101px;width:805px;height:231px;background:var(--note);border-radius:20px}

  .year{position:absolute;left:58px;top:366px;width:806px;display:grid;grid-template-columns:repeat(4,180px);column-gap:29px;row-gap:8px}
  .month h2{font-family:"Kaushan Script","Yellowtail",cursive;font-weight:400;font-size:18px;text-align:center;color:var(--ink);height:24px;line-height:24px}
  .weekdays{display:grid;grid-template-columns:repeat(7,1fr);background:var(--ink);border-radius:7px;height:17px;align-items:center;padding:0 4px}
  .weekdays span{font-family:"Roboto",sans-serif;font-weight:700;font-size:7.5px;color:var(--white);text-align:center}
  .dates{display:grid;grid-template-columns:repeat(7,1fr);grid-auto-rows:1fr;height:124px;background:var(--note);border-radius:0 0 10px 10px;padding:6px 4px 4px;margin-top:-2px}
  .dates span{font-family:"Roboto",sans-serif;font-style:italic;font-weight:700;font-size:9px;color:var(--ink);text-align:center;display:flex;align-items:center;justify-content:center}

  .facts{position:absolute;left:0;top:915px;width:921px;height:245px;background:var(--band)}
  .num,.note{position:absolute;margin:0}
  .num{line-height:1;white-space:nowrap}
  .num.thin{font-family:"Roboto",sans-serif;font-weight:300}
  .num.bold{font-family:"Playfair Display",serif;font-weight:900;font-variant-numeric:lining-nums}
  .note{font-family:"Lora",serif;font-style:italic;font-size:10px;line-height:1.2;color:var(--white)}
  .note.center{text-align:center}
  .note.sans{font-family:"Roboto",sans-serif;font-style:normal;font-size:11.5px;line-height:1.2}
  .note.strong{font-family:"Roboto",sans-serif;font-style:italic;font-weight:900;font-size:13.5px;line-height:1.28}

  .n-events{left:63px;top:33px;font-size:78px;color:var(--sky)}
  .c-events{left:154px;top:45px;width:90px}

  .n-kisses{left:60px;top:109px;width:180px;text-align:center;font-size:76px;letter-spacing:-2px;color:var(--lemon)}
  .c-kisses{left:56px;top:190px;width:188px}

  .n-self{left:265px;top:17px;font-size:118px;color:var(--magenta)}
  .c-self{left:262px;top:133px;width:90px}

  .n-friends{left:375px;top:30px;font-size:64px;color:var(--lemon)}
  .c-friends{left:457px;top:41px;width:96px}

  .n-meals{left:362px;top:107px;width:160px;text-align:center;font-size:76px;color:var(--sky)}
  .c-meals{left:362px;top:177px;width:160px}

  .n-work{left:562px;top:32px;width:150px;text-align:center;font-size:72px;color:var(--orange)}
  .c-work{left:562px;top:98px;width:150px}

  .n-coffee{left:538px;top:138px;font-size:78px;color:var(--red)}
  .c-coffee{left:630px;top:152px;width:84px}

  .n-dates{left:733px;top:19px;font-size:106px;color:var(--lime)}
  .c-dates{left:733px;top:131px;width:132px}
</style>
</head>
<body>
<main class="poster">
  <header class="headline">
    <span class="rule"></span>
    <h1>These are the days</h1>
    <span class="rule"></span>
  </header>

  <section class="wishes" aria-label="Space for handwritten advice"></section>

  <section class="year">
    <div class="month"><h2>December 2019</h2>
      <div class="weekdays"><span>SUN</span><span>MON</span><span>TUE</span><span>WED</span><span>THU</span><span>FRI</span><span>SAT</span></div>
      <div class="dates"><span style="grid-column:1">1</span><span>2</span><span>3</span><span>4</span><span>5</span><span>6</span><span>7</span><span>8</span><span>9</span><span>10</span><span>11</span><span>12</span><span>13</span><span>14</span><span>15</span><span>16</span><span>17</span><span>18</span><span>19</span><span>20</span><span>21</span><span>22</span><span>23</span><span>24</span><span>25</span><span>26</span><span>27</span><span>28</span><span>29</span><span>30</span><span>31</span></div>
    </div>
    <div class="month"><h2>January 2020</h2>
      <div class="weekdays"><span>SUN</span><span>MON</span><span>TUE</span><span>WED</span><span>THU</span><span>FRI</span><span>SAT</span></div>
      <div class="dates"><span style="grid-column:4">1</span><span>2</span><span>3</span><span>4</span><span>5</span><span>6</span><span>7</span><span>8</span><span>9</span><span>10</span><span>11</span><span>12</span><span>13</span><span>14</span><span>15</span><span>16</span><span>17</span><span>18</span><span>19</span><span>20</span><span>21</span><span>22</span><span>23</span><span>24</span><span>25</span><span>26</span><span>27</span><span>28</span><span>29</span><span>30</span><span>31</span></div>
    </div>
    <div class="month"><h2>February 2020</h2>
      <div class="weekdays"><span>SUN</span><span>MON</span><span>TUE</span><span>WED</span><span>THU</span><span>FRI</span><span>SAT</span></div>
      <div class="dates"><span style="grid-column:7">1</span><span>2</span><span>3</span><span>4</span><span>5</span><span>6</span><span>7</span><span>8</span><span>9</span><span>10</span><span>11</span><span>12</span><span>13</span><span>14</span><span>15</span><span>16</span><span>17</span><span>18</span><span>19</span><span>20</span><span>21</span><span>22</span><span>23</span><span>24</span><span>25</span><span>26</span><span>27</span><span>28</span><span>29</span></div>
    </div>
    <div class="month"><h2>March 2020</h2>
      <div class="weekdays"><span>SUN</span><span>MON</span><span>TUE</span><span>WED</span><span>THU</span><span>FRI</span><span>SAT</span></div>
      <div class="dates"><span style="grid-column:1">1</span><span>2</span><span>3</span><span>4</span><span>5</span><span>6</span><span>7</span><span>8</span><span>9</span><span>10</span><span>11</span><span>12</span><span>13</span><span>14</span><span>15</span><span>16</span><span>17</span><span>18</span><span>19</span><span>20</span><span>21</span><span>22</span><span>23</span><span>24</span><span>25</span><span>26</span><span>27</span><span>28</span><span>29</span><span>30</span><span>31</span></div>
    </div>
    <div class="month"><h2>April 2020</h2>
      <div class="weekdays"><span>SUN</span><span>MON</span><span>TUE</span><span>WED</span><span>THU</span><span>FRI</span><span>SAT</span></div>
      <div class="dates"><span style="grid-column:4">1</span><span>2</span><span>3</span><span>4</span><span>5</span><span>6</span><span>7</span><span>8</span><span>9</span><span>10</span><span>11</span><span>12</span><span>13</span><span>14</span><span>15</span><span>16</span><span>17</span><span>18</span><span>19</span><span>20</span><span>21</span><span>22</span><span>23</span><span>24</span><span>25</span><span>26</span><span>27</span><span>28</span><span>29</span><span>30</span></div>
    </div>
    <div class="month"><h2>May 2020</h2>
      <div class="weekdays"><span>SUN</span><span>MON</span><span>TUE</span><span>WED</span><span>THU</span><span>FRI</span><span>SAT</span></div>
      <div class="dates"><span style="grid-column:6">1</span><span>2</span><span>3</span><span>4</span><span>5</span><span>6</span><span>7</span><span>8</span><span>9</span><span>10</span><span>11</span><span>12</span><span>13</span><span>14</span><span>15</span><span>16</span><span>17</span><span>18</span><span>19</span><span>20</span><span>21</span><span>22</span><span>23</span><span>24</span><span>25</span><span>26</span><span>27</span><span>28</span><span>29</span><span>30</span><span>31</span></div>
    </div>
    <div class="month"><h2>June 2020</h2>
      <div class="weekdays"><span>SUN</span><span>MON</span><span>TUE</span><span>WED</span><span>THU</span><span>FRI</span><span>SAT</span></div>
      <div class="dates"><span style="grid-column:2">1</span><span>2</span><span>3</span><span>4</span><span>5</span><span>6</span><span>7</span><span>8</span><span>9</span><span>10</span><span>11</span><span>12</span><span>13</span><span>14</span><span>15</span><span>16</span><span>17</span><span>18</span><span>19</span><span>20</span><span>21</span><span>22</span><span>23</span><span>24</span><span>25</span><span>26</span><span>27</span><span>28</span><span>29</span><span>30</span></div>
    </div>
    <div class="month"><h2>July 2020</h2>
      <div class="weekdays"><span>SUN</span><span>MON</span><span>TUE</span><span>WED</span><span>THU</span><span>FRI</span><span>SAT</span></div>
      <div class="dates"><span style="grid-column:4">1</span><span>2</span><span>3</span><span>4</span><span>5</span><span>6</span><span>7</span><span>8</span><span>9</span><span>10</span><span>11</span><span>12</span><span>13</span><span>14</span><span>15</span><span>16</span><span>17</span><span>18</span><span>19</span><span>20</span><span>21</span><span>22</span><span>23</span><span>24</span><span>25</span><span>26</span><span>27</span><span>28</span><span>29</span><span>30</span><span>31</span></div>
    </div>
    <div class="month"><h2>August 2020</h2>
      <div class="weekdays"><span>SUN</span><span>MON</span><span>TUE</span><span>WED</span><span>THU</span><span>FRI</span><span>SAT</span></div>
      <div class="dates"><span style="grid-column:7">1</span><span>2</span><span>3</span><span>4</span><span>5</span><span>6</span><span>7</span><span>8</span><span>9</span><span>10</span><span>11</span><span>12</span><span>13</span><span>14</span><span>15</span><span>16</span><span>17</span><span>18</span><span>19</span><span>20</span><span>21</span><span>22</span><span>23</span><span>24</span><span>25</span><span>26</span><span>27</span><span>28</span><span>29</span><span>30</span><span>31</span></div>
    </div>
    <div class="month"><h2>September 2020</h2>
      <div class="weekdays"><span>SUN</span><span>MON</span><span>TUE</span><span>WED</span><span>THU</span><span>FRI</span><span>SAT</span></div>
      <div class="dates"><span style="grid-column:3">1</span><span>2</span><span>3</span><span>4</span><span>5</span><span>6</span><span>7</span><span>8</span><span>9</span><span>10</span><span>11</span><span>12</span><span>13</span><span>14</span><span>15</span><span>16</span><span>17</span><span>18</span><span>19</span><span>20</span><span>21</span><span>22</span><span>23</span><span>24</span><span>25</span><span>26</span><span>27</span><span>28</span><span>29</span><span>30</span></div>
    </div>
    <div class="month"><h2>October 2020</h2>
      <div class="weekdays"><span>SUN</span><span>MON</span><span>TUE</span><span>WED</span><span>THU</span><span>FRI</span><span>SAT</span></div>
      <div class="dates"><span style="grid-column:5">1</span><span>2</span><span>3</span><span>4</span><span>5</span><span>6</span><span>7</span><span>8</span><span>9</span><span>10</span><span>11</span><span>12</span><span>13</span><span>14</span><span>15</span><span>16</span><span>17</span><span>18</span><span>19</span><span>20</span><span>21</span><span>22</span><span>23</span><span>24</span><span>25</span><span>26</span><span>27</span><span>28</span><span>29</span><span>30</span><span>31</span></div>
    </div>
    <div class="month"><h2>November 2020</h2>
      <div class="weekdays"><span>SUN</span><span>MON</span><span>TUE</span><span>WED</span><span>THU</span><span>FRI</span><span>SAT</span></div>
      <div class="dates"><span style="grid-column:1">1</span><span>2</span><span>3</span><span>4</span><span>5</span><span>6</span><span>7</span><span>8</span><span>9</span><span>10</span><span>11</span><span>12</span><span>13</span><span>14</span><span>15</span><span>16</span><span>17</span><span>18</span><span>19</span><span>20</span><span>21</span><span>22</span><span>23</span><span>24</span><span>25</span><span>26</span><span>27</span><span>28</span><span>29</span><span>30</span></div>
    </div>
  </section>

  <section class="facts">
    <span class="num thin n-events">12</span>
    <p class="note c-events">The number of events you'll run if you coordinate one each month.</p>

    <span class="num bold n-kisses">1460</span>
    <p class="note center c-kisses">the number of kisses given if you kiss each kid just once a day.</p>

    <span class="num bold n-self">4</span>
    <p class="note sans c-self">The number of days devoted entirely to you, if you take two hours a week just for yourself.</p>

    <span class="num bold n-friends">52</span>
    <p class="note c-friends">The people you've made time for if you meet with just one friend each week</p>

    <span class="num thin n-meals">260</span>
    <p class="note center c-meals">The number of family meals shared together if you have just 5 dinners a week.</p>

    <span class="num thin n-work">156</span>
    <p class="note center c-work">The number of workouts you can squeeze in if you just do it three times a week.</p>

    <span class="num bold n-coffee">24</span>
    <p class="note c-coffee">The number of cups of coffee shared together if you have just 5 dinners a week.</p>

    <span class="num bold n-dates">20</span>
    <p class="note strong c-dates">about the number of dates you could go on with Avery if you got out every few weeks</p>
  </section>
</main>
</body>
</html>
```